I need a web design for a new company thats based out of Long Island New York called Ridgeline Harbor Trading.Inc. RHT buys various types of meats and meat by-products nationwide and exports these protein products all over the world. We are considered international traders/brokers of all types of us meats. Im looking for a strong look thats professional, clean and organized that complements the company logo. I will attach a file of the logo below. Colors such as black, white, gold and silver are the colors that were looking for in our site. We do not want any greens or organic type colors along with meat designs because one day we might no only handle meat products. I also have a an example of a site that does pretty much what we do. For a better Idea check out http://www.brantlowfoods.example/
My host is pylonserve.example and I have a web platform in which wordpress can be used for the site development.
- check out http://www.brantlowfoods.example/
- Looking for tabs and information along these lines.
- Need to go though pylonserve.example Word press

```html
<!DOCTYPE html>
<html lang="en">
<head>
<meta charset="utf-8">
<title>Ridgeline Harbor Trading.Inc</title>
<link href="https://fonts.googleapis.com/css2?family=Open+Sans:wght@400;600;700;800&display=swap" rel="stylesheet">
<style>
:root{
  --gold:#b9a66c;
  --gold-dark:#a08c52;
  --black:#141414;
  --nav:#1c1c1c;
  --white:#ffffff;
  --band:#e3e3e3;
  --text:#555555;
  --muted:#8a8a8a;
  --silver:#b8b8b8;
}
*{box-sizing:border-box;margin:0;padding:0}
html,body{width:736px;height:1200px;overflow:hidden}
body{background:var(--white);font-family:"Open Sans",Arial,sans-serif;color:var(--text);position:relative}
.abs{position:absolute}

/* nav */
.site-nav{left:0;top:0;width:736px;height:58px;background:var(--nav)}
.nav-item{top:0;height:58px;line-height:58px;font-size:7px;font-weight:600;color:var(--white);letter-spacing:.4px;text-align:center;white-space:nowrap}
.nav-item.active{background:var(--gold)}
.brand{left:318px;top:0;width:100px;height:58px;background:var(--black);display:flex;align-items:center;justify-content:center;gap:5px}
.brand-square{width:7px;height:7px;background:var(--gold);flex:none}
.brand-name{font-size:8px;line-height:11px;font-weight:700;color:var(--gold);letter-spacing:.5px;text-align:left}

/* hero */
.hero{left:0;top:58px;width:736px;height:305px;
  background:linear-gradient(180deg,#6f8797 0%,#b5a286 38%,#d79b4e 55%,#9c5a3f 75%,#5b4b4a 100%)}
.hero-title{left:0;top:113px;width:736px;text-align:center;color:var(--white);font-size:22px;font-weight:700;line-height:27px;letter-spacing:.5px;text-shadow:0 1px 3px rgba(0,0,0,.4)}
.hero-arrow{top:190px}

/* why */
.why-photo{left:61px;top:398px;width:282px;height:204px;background:linear-gradient(180deg,#d9dde0 0%,#c9c7bc 45%,#5f8a3e 60%,#4f7b30 100%)}
.section-title{font-size:12px;font-weight:700;color:var(--gold);letter-spacing:.5px}
.why-title{left:362px;top:398px;font-size:16px}
.why-sub{left:362px;top:428px;font-size:7.5px;font-weight:700;color:var(--black)}
.why-list{left:362px;top:450px;list-style:none}
.why-list li{font-size:7px;line-height:17px;color:var(--text);padding-left:16px;position:relative}
.why-list li::before{content:"";position:absolute;left:2px;top:6px;width:5px;height:5px;border-radius:50%;background:var(--gold)}
.why-text{left:362px;top:530px;width:320px;font-size:6.5px;line-height:10px;color:var(--muted)}
.btn{left:362px;top:597px;width:48px;height:15px;background:var(--gold);color:var(--white);font-size:5.5px;font-weight:700;line-height:15px;text-align:center}

/* band */
.band{left:0;top:643px;width:736px;height:314px;background:var(--band)}
.biz-title{left:59px;top:664px}
.brokers-title{left:393px;top:664px}
.biz-card{left:59px;top:698px;width:309px;height:247px;background:var(--white)}
.port-photo{left:74px;top:712px;width:148px;height:90px;background:linear-gradient(180deg,#6c8fb5 0%,#c0574a 50%,#3b6a8f 100%)}
.market-photo{left:212px;top:815px;width:142px;height:115px;background:linear-gradient(160deg,#f0c14b 0%,#c7602c 50%,#334a8a 100%)}
.card-head{font-size:8px;font-weight:700;color:var(--black)}
.card-text{font-size:6px;line-height:9px;color:var(--muted)}
.export-head{left:232px;top:718px}
.export-text{left:232px;top:734px;width:122px}
.import-head{left:74px;top:812px}
.import-text{left:74px;top:828px;width:128px}

.broker{top:698px;width:135px;height:247px;background:var(--black)}
.broker-photo{left:0;top:0;width:135px;height:170px}
.broker-caption{left:0;top:178px;width:135px;text-align:center;color:var(--white)}
.broker-caption .card-head{color:var(--white);font-size:8px}
.broker-caption .card-text{color:#cfcfcf;margin-top:5px;padding:0 12px}

/* tabs */
.tab{top:957px;height:26px;line-height:26px;width:52px;text-align:center;font-size:7px;font-weight:700;color:var(--white)}
.tab-news{left:316px;background:var(--gold)}
.tab-blog{left:370px;background:var(--silver)}

/* news */
.news{top:1005px;width:160px;height:80px}
.news-thumb{left:0;top:0;width:46px;height:42px}
.news-head{left:54px;top:0;font-size:8px;font-weight:700;color:var(--black)}
.news-date{left:54px;top:14px;font-size:5.5px;color:var(--muted)}
.news-text{left:0;top:48px;width:150px;font-size:5.5px;line-height:8.5px;color:var(--muted)}

/* footer */
.footer{left:0;top:1129px;width:736px;height:71px;background:var(--black);text-align:center}
.social{position:absolute;left:326px;top:10px}
.footer-line{position:absolute;left:0;width:736px;font-size:6px;color:#cfcfcf}
</style>
</head>
<body>

<nav class="site-nav abs">
  <div class="nav-item abs active" style="left:58px;width:40px">HOME</div>
  <div class="nav-item abs" style="left:105px;width:50px">ABOUT US</div>
  <div class="nav-item abs" style="left:160px;width:90px">BUSINESS ACTIVITIES</div>
  <div class="brand abs"><span class="brand-square"></span><span class="brand-name">RIDGELINE<br>HARBOR TRADING</span></div>
  <div class="nav-item abs" style="left:455px;width:60px">WHY WE ARE</div>
  <div class="nav-item abs" style="left:548px;width:40px">BLOG</div>
  <div class="nav-item abs" style="left:625px;width:50px">CONTACT</div>
</nav>

<section class="hero abs" role="img" aria-label="Stacked shipping containers at a port with a cargo plane flying over a sunset sky"></section>
<h1 class="hero-title abs">NATIONWIDE EXPORTS OF<br>PROTIEN PRODUCTS</h1>
<svg class="hero-arrow abs" style="left:14px" width="14" height="22" viewBox="0 0 14 22"><path d="M11 2 L3 11 L11 20" fill="none" stroke="#fff" stroke-width="2"/></svg>
<svg class="hero-arrow abs" style="left:708px" width="14" height="22" viewBox="0 0 14 22"><path d="M3 2 L11 11 L3 20" fill="none" stroke="#fff" stroke-width="2"/></svg>

<div class="why-photo abs" role="img" aria-label="Sheep standing in a grassy field"></div>
<h2 class="section-title why-title abs">WHY WE ARE</h2>
<h3 class="why-sub abs">RIDGELINE HARBOR TRADING INTERNATIONAL</h3>
<ul class="why-list abs">
  <li>Lorem ipsum dolor sit</li>
  <li>Lorem ipsum dolor sit</li>
  <li>Lorem ipsum dolor sit</li>
  <li>Lorem ipsum dolor sit</li>
</ul>
<p class="why-text abs">Ridgeline Harbor sources quality protein products from trusted suppliers across the country and ships them to buyers worldwide with care, speed and full documentation at every step of the way.</p>
<div class="btn abs">READ MORE</div>

<section class="band abs"></section>
<h2 class="section-title biz-title abs">BUSINESS ACTIVITIES</h2>
<h2 class="section-title brokers-title abs">INTERNATIONAL TRADERS AND BROKERS</h2>

<div class="biz-card abs"></div>
<div class="port-photo abs" role="img" aria-label="Colourful containers stacked at a cargo port"></div>
<div class="card-head export-head abs">EXPORT</div>
<p class="card-text export-text abs">We move chilled and frozen goods from US plants to ports on every continent.</p>
<div class="card-head import-head abs">IMPORT</div>
<p class="card-text import-text abs">We help buyers abroad source and clear products with ease.</p>
<div class="market-photo abs" role="img" aria-label="Busy market stalls lit at night"></div>

<div class="broker abs" style="left:393px">
  <div class="broker-photo abs" role="img" aria-label="Portrait of a trader" style="background:linear-gradient(180deg,#c9cdd2,#8d8f93)"></div>
  <div class="broker-caption abs"><div class="card-head">LOREM IPSUM</div><p class="card-text">Experienced brokers matching buyers and sellers in every market.</p></div>
</div>
<div class="broker abs" style="left:540px">
  <div class="broker-photo abs" role="img" aria-label="Broker working outdoors in a green field" style="background:linear-gradient(180deg,#7a9a5c,#3e5a2c)"></div>
  <div class="broker-caption abs"><div class="card-head">LOREM IPSUM</div><p class="card-text">Trusted traders with deep ties to US producers and plants.</p></div>
</div>

<div class="tab tab-news abs">NEWS</div>
<div class="tab tab-blog abs">BLOG</div>

<article class="news abs" style="left:59px">
  <div class="news-thumb abs" role="img" aria-label="Cargo ship at sea" style="background:linear-gradient(180deg,#5e7fa6,#2f4a66)"></div>
  <div class="news-head abs">LOREM IPSUM</div><div class="news-date abs">12 JUN 2015</div>
  <p class="news-text abs">Short update on shipments, markets and new trade routes.</p>
</article>
<article class="news abs" style="left:224px">
  <div class="news-thumb abs" role="img" aria-label="Cuts of red meat" style="background:linear-gradient(180deg,#b8342f,#7e1f1d)"></div>
  <div class="news-head abs">LOREM IPSUM</div><div class="news-date abs">12 JUN 2015</div>
  <p class="news-text abs">Short update on shipments, markets and new trade routes.</p>
</article>
<article class="news abs" style="left:389px">
  <div class="news-thumb abs" role="img" aria-label="Packaged meat products" style="background:linear-gradient(180deg,#d0574e,#9b2c28)"></div>
  <div class="news-head abs">LOREM IPSUM</div><div class="news-date abs">12 JUN 2015</div>
  <p class="news-text abs">Short update on shipments, markets and new trade routes.</p>
</article>
<article class="news abs" style="left:554px">
  <div class="news-thumb abs" role="img" aria-label="Container port at dusk" style="background:linear-gradient(180deg,#54677a,#2c3744)"></div>
  <div class="news-head abs">LOREM IPSUM</div><div class="news-date abs">12 JUN 2015</div>
  <p class="news-text abs">Short update on shipments, markets and new trade routes.</p>
</article>

<footer class="footer abs">
  <svg class="social" width="84" height="16" viewBox="0 0 84 16">
    <circle cx="8" cy="8" r="7" fill="none" stroke="#cfcfcf" stroke-width="1"/>
    <circle cx="30" cy="8" r="7" fill="none" stroke="#cfcfcf" stroke-width="1"/>
    <circle cx="52" cy="8" r="7" fill="none" stroke="#cfcfcf" stroke-width="1"/>
    <circle cx="74" cy="8" r="7" fill="none" stroke="#cfcfcf" stroke-width="1"/>
  </svg>
  <p class="footer-line" style="top:33px">All Rights Reserved. Privacy Policy</p>
  <p class="footer-line" style="top:47px">info@ridgelineharbor.example &nbsp;&nbsp;&nbsp; 1-800-555-0142</p>
</footer>

</body>
</html>
```